Need Help Rebranding My Food Blog

I have a Wordpress Food blog called BeetBuddies.com. Right now it has no life and is very bland. I am rebranding this site to a new named called, TheHoneyedDays.com. I would love to have a blog that is vibrant and full of life and personality.

One of my top priorities when a new visitor comes to my site is to quickly understand what the site is about (Gluten-free, dairy-free sweets that taste delicious).

I also want people to feel a connection with me when they come to the site.

Here are some other things that I'd like in the blog design...

1. Optin
My business is driven by adding people to my list so it is very important for me to have an optin front and center/ above-the-fold. See https://www.quietrevenuehub.com/ as an example. The headline that I would like is "Gluten-free & dairy-free sweets that actually taste good"

2. Vibrant/full life
The next important aspect of this blog is that it is vibrant. I like colors that remind me of a SUNSET. See attachments for logo and color scheme. Here's an example of a site I really like that is vibrant: http://www.mellowplateliving.com/

Also see Image titled: "Sample: Feeling". Notice the feeling you get from the image/brush strokes and how it feels light, breezy, and free spirited.

3. Food Images
The last important aspect for my blog is to showcase my recipes. I have attached a few of them as examples. Its really important for a food blog to showcase beautiful pictures of recipes for people to see so will definitely need this in the design.

Also, attached...
1. Image of me.
2. New logo for TheHoneyedDays (notice: don't use the one attached as "Sample/Feeling". That's just for reference of the feeling I like.)

Thanks!

Rosalind

P.S. I didn't include all the copy that would be needed so feel free to use the "lorem ipsum" text as placeholder if need be.

Target Market(s)

stay-at-home moms, dairy-free & gluten allergies, love desserts & sweets

Coding

Coded - Design and coding required

Font styles to use
Sans Serif

Requirements
Must have
• 1. Optin area with my picture and what I'm about ""Gluten-free & dairy-free sweets that actually taste good""
• 2. Must have personality/vibrancy to the site. Think full of life, not dull like my current website... beetbuddies.com
• 3. Highlight food images (Vertical image holders only)
Nice to have
• Color scheme should be based on my logo
Should not have
• No black or grey colors

```html
<!DOCTYPE html>
<html lang="en">
<head>
<meta charset="utf-8">
<title>The Honeyed Days</title>
<link rel="stylesheet" href="https://fonts.googleapis.com/css2?family=Roboto:wght@300;400;500;700&family=Great+Vibes&display=swap">
<style>
  :root {
    --blush: #fdbdb9;
    --blush-deep: #f7a9a6;
    --wine: #9c0a2b;
    --berry: #b3203e;
    --coral: #e86b78;
    --button: #e04a5c;
    --plum-dark: #3e1a36;
    --plum: #6b2a52;
    --white: #ffffff;
    --cocoa: #5e3434;
    --footer-head: #f0446a;
    --footer-text: #f6e6e2;
    --logo: #ef7a5e;
    --share-a: #3b5998;
    --share-b: #d34836;
    --share-c: #1da1f2;
    --share-d: #bd081c;
  }
  * { box-sizing: border-box; margin: 0; padding: 0; }
  html, body { width: 740px; height: 1200px; overflow: hidden; }
  body { font-family: "Roboto", Arial, sans-serif; background: var(--blush); position: relative; }
  .canvas { position: relative; width: 740px; height: 1200px; overflow: hidden; }

  /* Header */
  .site-header { position: absolute; left: 0; top: 0; width: 740px; height: 106px; background: var(--blush); }
  .brand { position: absolute; left: 45px; top: 36px; display: flex; align-items: center; gap: 8px;
           font-weight: 500; font-size: 24px; color: var(--logo); }
  .brand-dot { width: 12px; height: 12px; border-radius: 50%; background: var(--logo); }
  .main-nav { position: absolute; top: 42px; left: 0; width: 740px; }
  .main-nav a { position: absolute; font-size: 17px; font-weight: 700; color: var(--coral); text-decoration: none; }
  .main-nav a.is-active { color: var(--berry); border-bottom: 2px solid var(--berry); padding-bottom: 2px; }
  .search-icon { position: absolute; left: 658px; top: 44px; }

  /* Hero optin */
  .hero { position: absolute; left: 0; top: 106px; width: 740px; height: 247px;
          background: linear-gradient(100deg, var(--plum-dark) 0%, var(--plum) 55%, #5a2346 100%); }
  .hero-title { position: absolute; left: 0; width: 740px; top: 14px; text-align: center;
                color: var(--white); font-weight: 400; font-size: 38px; line-height: 45px; }
  .hero-button { position: absolute; left: 322px; top: 166px; width: 98px; height: 36px;
                 background: var(--button); color: var(--white); font-size: 15px; font-weight: 500;
                 display: flex; align-items: center; justify-content: center; }
  .hero-portrait { position: absolute; left: 590px; top: 0; width: 150px; height: 247px;
                   background: linear-gradient(160deg, #5b3343 0%, #c99a8f 45%, #efe6e0 100%); }
  .hero-arrow { position: absolute; top: 98px; }
  .hero-dots { position: absolute; top: 227px; left: 358px; display: flex; gap: 4px; }
  .hero-dots span { width: 9px; height: 9px; border-radius: 50%; border: 1.5px solid var(--white); }
  .hero-dots span.is-current { background: var(--white); }

  /* Featured recipe */
  .recipe { position: absolute; left: 0; top: 353px; width: 740px; height: 337px; background: var(--blush); }
  .recipe-title { position: absolute; left: 56px; top: 2px; font-size: 34px; font-weight: 500; color: var(--wine); }
  .recipe-meta { position: absolute; left: 60px; top: 44px; font-size: 12px; color: var(--coral); display: flex; gap: 14px; align-items: center; }
  .recipe-meta .date { display: flex; gap: 5px; align-items: center; }
  .recipe-excerpt { position: absolute; left: 60px; top: 88px; width: 362px; font-size: 13.4px; line-height: 17.2px;
                    font-weight: 500; color: var(--wine); }
  .recipe-button { position: absolute; left: 60px; top: 210px; width: 76px; height: 23px; background: var(--button);
                   color: var(--white); font-size: 13px; font-weight: 500; display: flex; align-items: center; justify-content: center; }
  .share-bar { position: absolute; left: 60px; top: 308px; height: 27px; display: flex; align-items: center; }
  .share-total { font-size: 11.5px; color: var(--coral); font-weight: 500; width: 72px; }
  .share-btn { height: 27px; width: 74px; margin-right: 2px; display: flex; align-items: center; justify-content: space-between;
               padding: 0 8px; color: var(--white); font-size: 12px; font-weight: 500; }
  .share-btn .label { font-size: 9px; font-weight: 400; }
  .share-a { background: var(--share-a); }
  .share-b { background: var(--share-b); }
  .share-c { background: var(--share-c); }
  .share-d { background: var(--share-d); }
  .recipe-photo { position: absolute; left: 480px; top: 0; width: 224px; height: 337px;
                  background: linear-gradient(160deg, #b7b0a8 0%, #e8786a 40%, #c6bdb2 70%, #ef6e64 100%); }
  .pin-square { position: absolute; left: 480px; top: 0; width: 30px; height: 20px; background: var(--share-d); }

  /* About */
  .about { position: absolute; left: 0; top: 690px; width: 740px; height: 303px; background: var(--white); }
  .about-art { position: absolute; left: 0; top: 0; width: 428px; height: 303px;
               background: radial-gradient(ellipse 48% 40% at 50% 50%, #b8468a 0%, #e07aa8 45%, #f6d6e2 75%, #ffffff 100%); }
  .about-title { position: absolute; left: 490px; top: 18px; font-size: 41px; font-weight: 500; color: var(--wine); }
  .about-subtitle { position: absolute; left: 491px; top: 64px; font-size: 16px; font-weight: 300; color: var(--coral); }
  .about-text { position: absolute; left: 492px; top: 104px; width: 190px; font-size: 13.4px; line-height: 16.5px;
                font-weight: 300; color: var(--wine); }
  .about-signature { position: absolute; left: 496px; top: 222px; font-family: "Great Vibes", cursive; font-size: 32px; color: var(--wine); }

  /* Footer */
  .site-footer { position: absolute; left: 0; top: 993px; width: 740px; height: 207px; background: var(--cocoa); }
  .footer-col { position: absolute; top: 32px; }
  .footer-col h3 { font-size: 16px; font-weight: 700; color: var(--footer-head); margin-bottom: 14px; }
  .footer-col a { display: block; font-size: 12.5px; font-weight: 500; color: var(--footer-text); text-decoration: none; margin-bottom: 14px; }
  .footer-social a { font-size: 14px; font-weight: 700; margin-bottom: 18px; }
  .footer-brand { position: absolute; left: 568px; top: 48px; font-size: 20px; font-weight: 500; color: var(--logo); }
  .footer-copy { position: absolute; left: 583px; top: 126px; font-size: 12px; font-weight: 300; line-height: 15px; color: var(--footer-text); }
  .to-top { position: absolute; left: 698px; top: 172px; }
</style>
</head>
<body>
<div class="canvas">

  <header class="site-header">
    <div class="brand"><span class="brand-dot"></span>TheHoneyedDays</div>
    <nav class="main-nav">
      <a class="is-active" href="#" style="left:301px">Home</a>
      <a href="#" style="left:366px">Recepie</a>
      <a href="#" style="left:448px">Blog</a>
      <a href="#" style="left:502px">About</a>
      <a href="#" style="left:567px">Contact</a>
    </nav>
    <svg class="search-icon" width="18" height="18" viewBox="0 0 18 18" aria-label="Search">
      <circle cx="7" cy="7" r="5" fill="none" stroke="#e86b78" stroke-width="2"/>
      <line x1="11" y1="11" x2="16" y2="16" stroke="#e86b78" stroke-width="2.5" stroke-linecap="round"/>
    </svg>
  </header>

  <section class="hero">
    <h1 class="hero-title">Gluten Free And<br>Dairy Free Sweets<br>That Actually Taste Good</h1>
    <div class="hero-button">Read More</div>
    <div class="hero-portrait" role="img" aria-label="Portrait of Rosalind smiling, holding a plate of cake and a fork"></div>
    <svg class="hero-arrow" style="left:22px" width="16" height="26" viewBox="0 0 16 26" aria-label="Previous slide">
      <polyline points="13,3 4,13 13,23" fill="none" stroke="#e0457a" stroke-width="4"/>
    </svg>
    <svg class="hero-arrow" style="left:704px" width="16" height="26" viewBox="0 0 16 26" aria-label="Next slide">
      <polyline points="3,3 12,13 3,23" fill="none" stroke="#e0457a" stroke-width="4"/>
    </svg>
    <div class="hero-dots"><span class="is-current"></span><span></span><span></span></div>
  </section>

  <section class="recipe">
    <h2 class="recipe-title">Water melon popsicles</h2>
    <div class="recipe-meta">
      <span>By Rosalind</span>
      <span class="date">
        <svg width="11" height="11" viewBox="0 0 11 11"><rect x="1" y="2" width="9" height="8" fill="none" stroke="#e86b78" stroke-width="1.3"/><line x1="1" y1="4.5" x2="10" y2="4.5" stroke="#e86b78" stroke-width="1.3"/></svg>
        January 2, 2017
      </span>
    </div>
    <p class="recipe-excerpt">There are many variations of passages of Lorem Ipsum available, but the majority have suffered alteration in some form, by injected humour, or randomised words which don't look even slightly believable. If you are going to use a passage of Lorem Ipsum, you need to be sure there isn't anything embarrassing hidden in the middle of text.</p>
    <div class="recipe-button">Read More</div>
    <div class="share-bar">
      <span class="share-total">123 Shares</span>
      <div class="share-btn share-a"><span class="label">Friendly</span><span>48</span></div>
      <div class="share-btn share-b"><span class="label">Circleup</span><span>44</span></div>
      <div class="share-btn share-c"><span class="label">Chirper</span><span>32</span></div>
      <div class="share-btn share-d"><span class="label">Pinwall</span><span>6</span></div>
    </div>
    <div class="recipe-photo" role="img" aria-label="Watermelon popsicles with watermelon wedges on a grey surface"></div>
    <div class="pin-square"></div>
  </section>

  <section class="about">
    <div class="about-art" role="img" aria-label="Pink and violet watercolour brush stroke behind the blog name"></div>
    <h2 class="about-title">About</h2>
    <p class="about-subtitle">The Honeyed Days</p>
    <p class="about-text">it is a long established fact that a reader will be distracted by the readable content of a page when looking at its layout. The point of using Lorem Ipsum is that it has a more-or-less normal</p>
    <p class="about-signature">Jane Doe</p>
  </section>

  <footer class="site-footer">
    <div class="footer-col" style="left:54px">
      <h3>FEATURES</h3>
      <a href="#">Home</a>
      <a href="#">Recepie</a>
      <a href="#">Blog</a>
    </div>
    <div class="footer-col" style="left:223px; top:34px">
      <h3>LEARN MORE</h3>
      <a href="#">Terms</a>
      <a href="#">About</a>
      <a href="#">Contact Us</a>
    </div>
    <div class="footer-col footer-social" style="left:420px; top:34px">
      <h3>#CONNECT</h3>
      <a href="#">Friendly</a>
      <a href="#">Chirper</a>
      <a href="#">Picturely</a>
    </div>
    <div class="footer-brand">TheHoneyedDays</div>
    <p class="footer-copy">© Copyright 2016<br>All Rights Reserved.</p>
    <svg class="to-top" width="24" height="24" viewBox="0 0 24 24" aria-label="Back to top">
      <circle cx="12" cy="12" r="10" fill="none" stroke="#f0446a" stroke-width="2"/>
      <polyline points="7,14 12,9 17,14" fill="none" stroke="#f0446a" stroke-width="2.2"/>
    </svg>
  </footer>

</div>
</body>
</html>
```